Seven Quiet Steps to Lift the Final Offer on YOUR House - MERVA Real Estate

I have written an E-Book that is called "Seven Quiet Steps to Lift the Final Offer on Your House." The E-Book will be available as a FREE download from my MERVA Real Estate landing page, and also from a Chatterly campaign that will be commencing in early September.

The E-Book content is in the WORD document below - I now need for it to be made to look more professional and suitable for publishing and placed on my landing page for download. Please review and send me some proposals for this e-book to be a bit more eye catching and appealing than just a WORD doc.

My MERVA Real Estate landing page is still under development and you can see the what is close to the final proposal here:

http://www.brell-tovan.com.au/merva/

The cover of the E-Book is at the bottom of the page. Please review and give the internals the sale look and feel.

Target Market(s)

Home and Property Owners in the middle ring Eastern Suburbs of Melbourne - approximately 15 - 30 km's from the central business district. The area is a very family oriented area and features mostly houses that are 3 or 4 bedroom - with some larger properties that are five or more bedrooms. The area is quite an expensive suburban community and house prices range between the low of $1,000,000 to a high of more than $2,500,000. The predominant cultural group that buys in this area are Chinese and Chinese Australian buyers. The predominant group who are selling are usually Australians of a white anglo-saxon background. Other groups are of Asian sub continent background (Indian / Sri Lankan/ Pakistan). All are families that are attracted to the area because of the great schools, good shopping, leisure facilities (parks, pools, courts etc), and excellent public and road transport infrastructure. Read the content of my e-book - it tells you every thing you need to know :)

Industry/Entity Type

Real Estate

Colors

Designer to choose colors to be used in the design.

Requirements
Must have
• Once completed the layout should not be too busy - it should be easy to read. I guess then the statement "less is more" is applicable.
• I will probably print a number of copies of this book for distribution as well - so please consider print attributes in the design.
• IMPORTANT: as for any e-book offering specialist advice, the MAIN reason for the book is for the generation of sales leads and to establish the author as a subject matter expert on the topic. Please consider this in your design elements. BUT - the book should also not come across as 1 big advertisement either. Subtle but impactful are well chosen words to describe how it should present.
Nice to have
• MERVA Real Estate branding on every page - to re-inforce the message.
Should not have
• No need for animations or illustrations/

```html
<!DOCTYPE html>
<html lang="en">
<head>
<meta charset="utf-8">
<title>Seven Quiet Steps to Lift the Final Offer on YOUR House - MERVA Real Estate</title>
<link href="https://fonts.googleapis.com/css2?family=Lato:ital,wght@0,400;0,700;0,900;1,400&family=Roboto+Condensed:wght@700&display=swap" rel="stylesheet">
<style>
  :root {
    --green: #3fbd92;
    --grey: #b4b4b4;
    --ink: #2a2a2a;
    --text: #3a3a3a;
    --paper: #ffffff;
    --canvas: #ffffff;
  }
  * { box-sizing: border-box; margin: 0; padding: 0; }
  html, body { width: 1200px; height: 1200px; overflow: hidden; background: var(--canvas); }
  body { position: relative; font-family: "Lato", sans-serif; color: var(--text); }

  .page {
    position: absolute; top: 216px; width: 542px; height: 766px;
    background: var(--paper);
    box-shadow: 0 1px 4px rgba(0,0,0,.25);
    overflow: hidden;
  }
  .page--left { left: 42px; }
  .page--right { left: 616px; }

  .page-header { position: absolute; top: 0; left: 0; width: 542px; height: 304px; }

  .brand { position: absolute; top: 30px; right: 31px; text-align: right; color: var(--ink); font-weight: 900; line-height: 1; }
  .brand__name { display: block; font-size: 58px; letter-spacing: -1px; }
  .brand__sub { display: block; font-size: 9px; letter-spacing: 11.2px; margin-top: 4px; margin-right: -11px; }

  .section-title {
    position: absolute; left: 33px; top: 320px;
    font-family: "Roboto Condensed", sans-serif; font-weight: 700;
    font-size: 16px; color: var(--green); letter-spacing: .2px;
  }
  .copy { position: absolute; left: 33px; width: 476px; font-size: 8px; line-height: 9.8px; }
  .copy p { margin-bottom: 10px; }
  .copy--intro { top: 348px; }
  .subhead { position: absolute; left: 33px; top: 517px; font-size: 9.8px; font-weight: 400; color: var(--green); }
  .bullets { position: absolute; left: 33px; top: 537px; width: 476px; list-style: none; font-size: 8px; line-height: 9.8px; }
  .bullets li { position: relative; padding-left: 9px; margin-bottom: 10px; }
  .bullets li::before { content: ""; position: absolute; left: 0; top: 3.5px; width: 3px; height: 3px; border-radius: 50%; background: var(--green); }
  .copy--closing { top: 659px; text-align: justify; }

  .pie { position: absolute; left: 32px; top: 332px; width: 220px; height: 220px; }
  .pie text { font-family: "Lato", sans-serif; font-size: 17px; fill: #fff; text-anchor: middle; }

  .buyer-col { position: absolute; left: 278px; top: 334px; width: 231px; font-size: 8px; line-height: 9.8px; text-align: justify; }
  .label { display: block; background: var(--green); color: #fff; font-size: 9.6px; line-height: 13px; padding-left: 6px; margin-bottom: 17px; text-align: left; }
  .buyer-col p { margin-bottom: 10px; }

  .notice { position: absolute; left: 33px; top: 592px; width: 476px; font-size: 8.4px; line-height: 11px; font-style: italic; }
  .notice strong { color: var(--green); font-style: normal; font-weight: 400; }
  .copy--outro { top: 634px; text-align: justify; }

  .page-footer { position: absolute; left: 0; top: 716px; width: 542px; height: 36px; }
  .page-footer text { font-family: "Lato", sans-serif; }
</style>
</head>
<body>

<section class="page page--left">
  <svg class="page-header" viewBox="0 0 677 380">
    <defs>
      <linearGradient id="skyFill" x1="0" y1="0" x2="1" y2="1">
        <stop offset="0" stop-color="#a9cfe0"/>
        <stop offset=".55" stop-color="#d9e4e3"/>
        <stop offset="1" stop-color="#e9d2b4"/>
      </linearGradient>
    </defs>
    <rect x="0" y="139" width="677" height="233" fill="url(#skyFill)" role="img" aria-label="Photo: agent in a suit writing on a tablet beside a rising red arrow over a city skyline"/>
    <polyline points="0,136 50,136 205,52 355,136 677,136" fill="none" stroke="var(--ink)" stroke-width="5"/>
    <rect x="0" y="371" width="677" height="7" fill="var(--ink)"/>
  </svg>
  <div class="brand"><span class="brand__name">MERVA</span><span class="brand__sub">REAL ESTATE</span></div>

  <h2 class="section-title">4. MARKETING AND ADVERTISING</h2>
  <div class="copy copy--intro">
    <p>Next to price - property marketing and advertising is the cause of the greatest amount of vendor stress. Marketing and advertising of residential property is expensive. It feels especially expensive when you are nervously waiting for the outcome of a sales campaign that will justify the cost.</p>
    <p>But don't worry. The right marketing campaign is of significant importance in order for the right buyer energy and activity to exist at the property throughout the campaign, and in order for that property to sell well. My friends at Tall Pine digital marketing – the agency with whom I entrust my own business website and Chatterly campaign marketing spend – measure the cost of marketing by "return on investment." Brilliant – nothing lightweight about that algorithm.</p>
    <p>The same formula is applied in real estate – marketing and advertising cost can simply be measured by the property owner's "return on investment" when the property sells at an above market price.</p>
    <p>There are plenty of agencies that will offer "free" marketing – usually a third or fourth tier internet only proposal that provides little exposure for the property and attracts a low number of buyers. These agencies charge a hefty sales commission if and when the home eventually sells – to recover the cost of the "free marketing." As with anything in life – cheapest is not always the best.</p>
  </div>
  <h3 class="subhead">An elite Agent will develop a premium price strategy for your home as follows:</h3>
  <ul class="bullets">
    <li>Create an exceptional marketing program that gets Buyers to the front door of the home. The foundation of exceptional marketing is beautiful photography, professional and descriptive copywriting, and accurate and clearly drawn floor plans.</li>
    <li>With Buyers at the front door of the home – the elite Agent will obtain their personal and contact details and then get them inside to experience and connect with the property features, layout and presentation on an emotional level.</li>
    <li>The elite Agent will then qualify and then create competition amongst emotionally engaged buyers using high-level negotiation skills.</li>
    <li>And finally – the elite Agent will conclude the sale having achieved a price from a winning buyer that defies logic – a price that is purely based on emotion, competition and the fear of loss.</li>
  </ul>
  <div class="copy copy--closing">
    <p>The general guideline for marketing is that a vendor should commit 1% of the logical sale price of the property. That means for a $1.4m home – an approximate guide for the marketing and advertising budget should be $14,000. A good agent will try and reduce the marketing outlay by not spending more than is necessary, but also achieve the best result.</p>
  </div>

  <svg class="page-footer" viewBox="0 0 677 45" aria-hidden="true">
    <rect x="0" y="15" width="620" height="16" fill="var(--green)"/>
    <rect x="0" y="31" width="677" height="12" fill="var(--ink)"/>
    <path d="M572,43 L603,8 Q609,2 617,2 L677,2 L677,43 Z" fill="var(--ink)"/>
    <text x="245" y="26.5" font-size="9" fill="#fff" letter-spacing="3.2">www.mervarealestate.com.au</text>
    <text x="623" y="31" font-size="20" fill="var(--green)">07</text>
  </svg>
</section>

<section class="page page--right">
  <svg class="page-header" viewBox="0 0 677 380">
    <defs>
      <linearGradient id="houseFill" x1="0" y1="0" x2="0" y2="1">
        <stop offset="0" stop-color="#5b8fd0"/>
        <stop offset=".45" stop-color="#9a8f7e"/>
        <stop offset=".75" stop-color="#7a5a44"/>
        <stop offset="1" stop-color="#4f6a3a"/>
      </linearGradient>
    </defs>
    <rect x="0" y="139" width="677" height="233" fill="url(#houseFill)" role="img" aria-label="Photo: two-storey brick family house with a garage, garden and tall trees at dusk"/>
    <polyline points="0,136 50,136 205,52 355,136 677,136" fill="none" stroke="var(--ink)" stroke-width="5"/>
    <rect x="0" y="371" width="677" height="7" fill="var(--ink)"/>
  </svg>
  <div class="brand"><span class="brand__name">MERVA</span><span class="brand__sub">REAL ESTATE</span></div>

  <svg class="pie" viewBox="0 0 220 220" role="img" aria-label="Pie chart of four buyer categories: Local, Out of Area, Passive, Active">
    <path d="M108.5,108.5 L108.5,2 A106.5,106.5 0 0 0 2,108.5 Z" fill="var(--grey)"/>
    <path d="M111.5,108.5 L218,108.5 A106.5,106.5 0 0 0 111.5,2 Z" fill="var(--green)"/>
    <path d="M108.5,111.5 L2,111.5 A106.5,106.5 0 0 0 108.5,218 Z" fill="var(--green)"/>
    <path d="M111.5,111.5 L111.5,218 A106.5,106.5 0 0 0 218,111.5 Z" fill="var(--grey)"/>
    <text x="63" y="75">Local</text>
    <text x="153" y="64">Out of</text>
    <text x="153" y="84">Area</text>
    <text x="63" y="156">Passive</text>
    <text x="153" y="156">Active</text>
  </svg>

  <div class="buyer-col">
    <span class="label">There are four buyer categories as follows:</span>
    <p>A premium price marketing strategy will capture each buyer segment so that 100% of the four possible buyer groups have the opportunity to be introduced to the property.</p>
    <p>Normally this involves a combination of Internet advertising on the biggest real estate portals – homefinder.com.au and estatelist.com.au (Active Buyers), combined with some form of print advertising (Passive Buyers).</p>
    <p>This ensures that the advertising "net" is thrown far enough that it captures and brings every type of Buyer to the property. This is also where the largest marketing cost is – the actual advertising of the property on the online portals and in print media.</p>
    <p>Other smaller cost, but equally important marketing vehicles are – AUCTION and/or FOR SALE boards outside the house featuring photo's showing a glimpse of the inside of the property; property brochures for buyers to take away with them at open for inspections so as to remind them of all the attributes and personality that the house had to offer.</p>
  </div>

  <p class="notice"><strong>IMPORTANT:</strong> the sale of your property is not in ISOLATION; it is in COMPETITION with other similar properties that are selling at the same time.</p>

  <div class="copy copy--outro">
    <p>I have personally seen vendors lose tens of thousands of dollars on price because they insisted on saving a few thousand dollars on marketing at the start of a campaign.</p>
    <p>Marketing and advertising for the sale of your property should be seen as an investment in price success – and like any investment, by attracting the right buyers to your property you should expect to see much more in profit return than your initial investment in marketing.</p>
  </div>

  <svg class="page-footer" viewBox="0 0 677 45" aria-hidden="true">
    <rect x="0" y="15" width="620" height="16" fill="var(--green)"/>
    <rect x="0" y="31" width="677" height="12" fill="var(--ink)"/>
    <path d="M572,43 L603,8 Q609,2 617,2 L677,2 L677,43 Z" fill="var(--ink)"/>
    <text x="245" y="26.5" font-size="9" fill="#fff" letter-spacing="3.2">www.mervarealestate.com.au</text>
    <text x="623" y="31" font-size="20" fill="var(--green)">08</text>
  </svg>
</section>

</body>
</html>
```